pharmacy/travel clinic business card design

We need a business card for our new business called Brenwick Travel Clinic and Pharmacy. Our primary focus is doing consultations for people before travelling internationally and providing vaccinations and prescriptions for them. While the business is considered a pharmacy, it has more the look and feel of a doctor's office. The design should communicate a professional and trustworthy feel. I have attached a copy of the logo we are going to be using.
Updates
Thanks for the submissions.  If you haven`t been eliminated you are one of the finalists.  Decision will likely be made tomorrow.

Target Market(s)
Customers, other health care professionals, travel agents
Industry/Entity Type
Clinic
Look and feel
Each slider illustrates characteristics of the customer's brand and the style your logo design should communicate.

```html
<!DOCTYPE html>
<html lang="en">
<head>
<meta charset="utf-8">
<title>Brenwick Travel Clinic and Pharmacy – Business Cards</title>
<link rel="stylesheet" href="https://fonts.googleapis.com/css2?family=Montserrat:wght@400;600&display=swap">
<style>
  :root {
    --sheet: #9a9a9a;
    --paper: #ffffff;
    --ink-dark: #000000;
    --brand-green: #7ed321;
    --brand-blue: #1e9be8;
    --rule: #bdbdbd;
    --meta: #8a8a8a;
  }
  * { box-sizing: border-box; margin: 0; padding: 0; }
  html, body { width: 1200px; height: 670px; overflow: hidden; }
  body {
    background: var(--sheet);
    position: relative;
    font-family: "Montserrat", Arial, sans-serif;
  }
  .card {
    position: absolute;
    width: 554px;
    height: 292px;
    overflow: hidden;
  }
  .card--light { background: var(--paper); }
  .card--dark { background: var(--ink-dark); }
  .card--front-light { left: 36px; top: 26px; }
  .card--back-light { left: 610px; top: 23px; }
  .card--front-dark { left: 36px; top: 353px; }
  .card--back-dark { left: 610px; top: 349px; }

  .brand {
    position: absolute;
    display: flex;
    align-items: flex-start;
    gap: 8px;
    color: var(--brand-green);
    font-weight: 600;
    line-height: 1;
  }
  .brand__dot {
    flex: none;
    border-radius: 50%;
    background: var(--brand-blue);
  }
  .brand__name { display: flex; flex-direction: column; }
  .brand__line--main { letter-spacing: -0.5px; white-space: nowrap; }
  .brand__line--sub { white-space: nowrap; }

  .brand--large { font-size: 34px; }
  .brand--large .brand__dot { width: 22px; height: 22px; margin-top: 4px; }
  .brand--large .brand__line--sub { font-size: 13px; margin-top: 3px; }

  .brand--small { font-size: 21px; }
  .brand--small .brand__dot { width: 15px; height: 15px; margin-top: 2px; }
  .brand--small .brand__line--sub { font-size: 9px; margin-top: 2px; }

  .card--front-light .brand { left: 253px; top: 40px; }
  .card--front-dark .brand { left: 157px; top: 62px; }
  .card--back-light .brand,
  .card--back-dark .brand { left: 98px; top: 104px; }

  .wave-band {
    position: absolute;
    left: 0;
    width: 554px;
  }
  .card--front-light .wave-band {
    top: 190px; height: 102px;
    background: linear-gradient(to bottom, rgba(30,155,232,0) 0%, rgba(30,155,232,0.28) 45%, rgba(30,155,232,0.45) 70%, rgba(30,155,232,0.1) 100%);
  }
  .card--front-dark .wave-band {
    top: 168px; height: 124px;
    background: linear-gradient(to bottom, rgba(30,155,232,0) 0%, rgba(30,155,232,0.3) 50%, rgba(30,155,232,0.55) 75%, rgba(30,155,232,0.15) 100%);
  }

  .hands-art {
    position: absolute;
    left: 0; top: 130px;
    width: 212px; height: 124px;
    background: radial-gradient(ellipse at 50% 55%, rgba(126,211,33,0.4), rgba(126,211,33,0) 70%);
  }

  .divider {
    position: absolute;
    left: 317px; top: 91px;
    width: 1px; height: 111px;
    background: var(--rule);
  }
  .contact { position: absolute; left: 341px; top: 72px; color: var(--meta); }
  .card--back-dark .contact { top: 74px; }
  .contact__name { font-size: 12px; font-weight: 400; letter-spacing: 0.2px; }
  .contact__lines { margin: 20px 0 0 20px; list-style: none; font-size: 9px; line-height: 1.35; }
</style>
</head>
<body>

  <section class="card card--light card--front-light">
    <div class="wave-band" role="img" aria-label="Flowing blue wave-line decoration"></div>
    <div class="hands-art" role="img" aria-label="Line illustration of caring hands clasped together"></div>
    <div class="brand brand--large">
      <span class="brand__dot"></span>
      <span class="brand__name">
        <span class="brand__line--main">Brenwick</span>
        <span class="brand__line--main">Travel Clinic</span>
        <span class="brand__line--sub">and Pharmacy</span>
      </span>
    </div>
  </section>

  <section class="card card--light card--back-light">
    <div class="brand brand--small">
      <span class="brand__dot"></span>
      <span class="brand__name">
        <span class="brand__line--main">Brenwick</span>
        <span class="brand__line--main">Travel Clinic</span>
        <span class="brand__line--sub">and Pharmacy</span>
      </span>
    </div>
    <div class="divider"></div>
    <div class="contact">
      <p class="contact__name">XYXYXYX XYXYXY</p>
      <ul class="contact__lines">
        <li>Xsdfsdfsdfdsfsdf</li>
        <li>Xsdfsdfsdfdsfsdf</li>
        <li>Xsdfsdfsdfdsfsdf</li>
      </ul>
    </div>
  </section>

  <section class="card card--dark card--front-dark">
    <div class="wave-band" role="img" aria-label="Flowing blue wave-line decoration"></div>
    <div class="brand brand--large">
      <span class="brand__dot"></span>
      <span class="brand__name">
        <span class="brand__line--main">Brenwick</span>
        <span class="brand__line--main">Travel Clinic</span>
        <span class="brand__line--sub">and Pharmacy</span>
      </span>
    </div>
  </section>

  <section class="card card--dark card--back-dark">
    <div class="brand brand--small">
      <span class="brand__dot"></span>
      <span class="brand__name">
        <span class="brand__line--main">Brenwick</span>
        <span class="brand__line--main">Travel Clinic</span>
        <span class="brand__line--sub">and Pharmacy</span>
      </span>
    </div>
    <div class="contact">
      <p class="contact__name">XYXYXYX XYXYXY</p>
      <ul class="contact__lines">
        <li>Xsdfsdfsdfdsfsdf</li>
        <li>Xsdfsdfsdfdsfsdf</li>
        <li>Xsdfsdfsdfdsfsdf</li>
      </ul>
    </div>
  </section>

</body>
</html>
```